2 Social Media Ads for Veltrane Kestrel - Final Deliver 8 Sizes

We are looking for a designer that can build out two separate ads focused on what we do and deliver those two ads in 8 files of various sizes. We need 2 Facebook (1200x630), 2 Twitter(506 x 253), 2 Instagram (2048x2048), and 2 verticle ads (1080x1920).

The two ads will focus on:
1. White Label Consulting for Veltrane Partners
- http://harwickadvisorsteam-dev.fernhostsites.example/consulting/white-label-consulting/ - website for ad copy.

2: Lumbrelix - A Orbiteo 720 Add-On for GDPR Compliance
Our tool helps you manage your GDPR data within Orbiteo 720. Your customers are aware of their right to be forgotten, how are your keeping that data up-to-date in Orbiteo 720? Whether that’s deleting, redacting or scrubbing that data, our tool takes these manual process and automates it with advanced algorithms and data processing rules. --- Possible Ad Copy

Delivery: AI with Layers, or PSD with Layers.

Target Market(s)

Veltrane Partners - Orbiteo QR, Orbiteo Lek, Orbiteo TK, Veltrane Partners without a focus on Orbiteo 720. Looking to expand product offerings and their business.

Industry/Entity Type

Information Technology

Font styles to use
Sans Serif

Requirements
Must have
• CALL TO ACTION: VISIT US AT BOOTH #1700
• 8 files of various sizes. We need 2 Facebook (1200x630), 2 Twitter(506 x 253), 2 Instagram (2048x2048), and 2 verticle ads (1080x1920).
Nice to have
• Images of Las Vegas, Images of Veltrane Conferences or People

```html
<!DOCTYPE html>
<html lang="en">
<head>
<meta charset="utf-8">
<title>Industry Leaders in White Label Consulting – Ad Set</title>
<link rel="stylesheet" href="https://fonts.googleapis.com/css2?family=Archivo+Black&family=Oswald:wght@600&family=Roboto:ital,wght@0,300;0,400;0,700;0,900;1,400;1,900&display=swap">
<style>
:root{
  --board:#b78f28;
  --green:#3fbf8f;
  --green-dark:#1f7d5a;
  --ink:#0b0b0b;
  --paper:#ffffff;
  --mist:#e9e9e9;
  --graphite:#4a4a4a;
  --photo-a:#dfe3e6;
  --photo-b:#9aa3ab;
}
*{box-sizing:border-box;margin:0;padding:0}
html,body{width:1200px;height:1058px;overflow:hidden}
body{background:var(--board);position:relative;font-family:"Roboto",Arial,sans-serif;color:var(--ink)}
.ad{position:absolute;overflow:hidden}
.abs{position:absolute}
.headline{font-family:"Archivo Black","Arial Black",sans-serif;line-height:1;letter-spacing:-.01em;white-space:nowrap}
.photo{position:absolute;background:linear-gradient(135deg,var(--photo-a),var(--photo-b))}
.brand{font-family:"Roboto",Arial,sans-serif;font-weight:300;color:var(--ink);line-height:1.2;display:flex;align-items:center;gap:6px}
.brand-dot{border-radius:50%;background:var(--ink);flex:none}
.num{color:var(--green)}

/* Facebook */
.ad-facebook{left:58px;top:50px;width:389px;height:204px;background:var(--paper)}
.ad-facebook .photo{left:0;top:0;width:200px;height:204px}
.ad-facebook .title-box{left:153px;top:21px;width:231px;height:111px;background:var(--green);border-radius:0 0 0 10px;text-align:right;padding:4px 8px 0 0}
.ad-facebook .headline{font-size:47px;color:var(--paper)}
.ad-facebook .leaders{font-size:23px;font-weight:400;line-height:1.1;margin-right:14px}
.ad-facebook .wlc{font-family:"Oswald",sans-serif;font-weight:600;font-size:18px;color:var(--paper);line-height:1.25;margin-right:10px}
.ad-facebook .booth{left:218px;top:132px;width:166px;height:34px;background:var(--ink);border-radius:0 0 12px 12px;color:var(--paper);text-align:right;padding:2px 10px 0 0}
.ad-facebook .booth small{display:block;font-size:9px;font-weight:700;line-height:1}
.ad-facebook .booth b{font-size:20px;font-weight:900;line-height:1.1}
.ad-facebook .brand{left:300px;top:170px;font-size:9px;font-weight:400;line-height:1.15;gap:4px}
.ad-facebook .brand-dot{width:7px;height:7px}

/* Twitter */
.ad-twitter{left:558px;top:172px;width:164px;height:82px;background:var(--paper)}
.ad-twitter .photo{left:0;top:0;width:40px;height:82px}
.ad-twitter .title-box{left:37px;top:2px;width:124px;height:52px;background:var(--green);border-radius:0 0 0 6px;text-align:right;padding:2px 4px 0 0}
.ad-twitter .headline{font-size:24px;color:var(--paper)}
.ad-twitter .leaders{font-size:12px;line-height:1.05;margin-right:16px}
.ad-twitter .wlc{font-family:"Oswald",sans-serif;font-weight:600;font-size:9px;color:var(--paper);line-height:1.25;margin-right:8px}
.ad-twitter .booth{left:76px;top:54px;width:85px;height:23px;background:var(--ink);border-radius:0 0 6px 6px;color:var(--paper);text-align:right;padding:3px 5px 0 0}
.ad-twitter .booth small{display:block;font-size:5px;font-weight:700;line-height:1.1}
.ad-twitter .booth b{display:block;font-size:11px;font-weight:900;line-height:1.1}

/* Instagram */
.ad-square{left:58px;top:343px;width:663px;height:663px;background:var(--mist)}
.ad-square .headline{left:94px;top:18px;font-size:124px}
.ad-square .tab{left:60px;top:121px;width:493px;height:86px;background:var(--ink);border-radius:30px 0 0 0;text-align:right;padding:4px 24px 0 0}
.ad-square .leaders{font-size:46px;color:var(--green);line-height:1}
.ad-square .wlc{font-family:"Archivo Black",sans-serif;font-size:32px;color:var(--paper);line-height:1.2}
.ad-square .frame{left:60px;top:206px;width:591px;height:346px;background:var(--ink);border-radius:0 40px 0 40px}
.ad-square .photo{left:67px;top:213px;width:577px;height:332px;border-radius:0 34px 0 34px}
.ad-square .booth{left:268px;top:549px;width:384px;height:77px;background:linear-gradient(90deg,var(--ink),var(--graphite));border-radius:0 0 36px 30px;color:var(--paper);text-align:right;padding:4px 26px 0 0}
.ad-square .booth small{display:block;font-size:22px;font-weight:700;line-height:1.05}
.ad-square .booth b{font-size:47px;font-weight:900;line-height:1}
.ad-square .brand{left:40px;top:566px;font-size:21px;gap:12px}
.ad-square .brand-dot{width:18px;height:18px}

/* Vertical */
.ad-vertical{left:799px;top:385px;width:350px;height:620px;background:var(--paper)}
.ad-vertical .brand{left:8px;top:12px;font-size:13px}
.ad-vertical .brand-dot{width:12px;height:12px}
.ad-vertical .headline{left:20px;top:55px;font-size:66px}
.ad-vertical .tab{left:7px;top:114px;width:290px;height:70px;background:var(--ink);border-radius:20px 0 0 0;text-align:right;padding:2px 8px 0 0}
.ad-vertical .leaders{font-size:40px;color:var(--green);line-height:1}
.ad-vertical .wlc{font-family:"Archivo Black",sans-serif;font-size:19px;color:var(--paper);line-height:1.35}
.ad-vertical .frame{left:7px;top:183px;width:334px;height:217px;background:var(--ink);border-radius:0 26px 0 26px}
.ad-vertical .photo{left:12px;top:188px;width:324px;height:207px;border-radius:0 22px 0 22px}
.ad-vertical .help{left:56px;top:398px;width:285px;height:156px;background:linear-gradient(180deg,var(--ink),var(--graphite));padding:8px 0 0 30px;color:var(--paper)}
.ad-vertical .help h2{font-size:16px;font-weight:400;color:var(--green);margin-left:-2px;margin-bottom:4px}
.ad-vertical .help ul{list-style:none}
.ad-vertical .help li{font-size:15px;font-style:italic;line-height:19.5px;padding-left:16px;position:relative}
.ad-vertical .help li b{font-weight:900}
.ad-vertical .help li::before{content:"";position:absolute;left:0;top:6px;width:9px;height:9px;background:var(--green);clip-path:polygon(0 0,100% 0,100% 60%,50% 100%,0 60%)}
.ad-vertical .booth{left:56px;top:552px;width:285px;height:60px;background:linear-gradient(180deg,var(--green),var(--green-dark));border-radius:0 0 26px 22px;text-align:right;padding:3px 18px 0 0}
.ad-vertical .booth small{display:block;font-size:16px;font-weight:700;line-height:1.05;color:var(--ink)}
.ad-vertical .booth b{font-size:35px;font-weight:900;line-height:1;color:var(--paper)}
</style>
</head>
<body>

<section class="ad ad-facebook" aria-label="Facebook ad">
  <div class="photo" role="img" aria-label="Photo of business people talking in a bright office"></div>
  <div class="abs title-box">
    <div class="headline">Industry</div>
    <div class="leaders">Leaders in</div>
    <div class="wlc">White Label Consulting</div>
  </div>
  <div class="abs booth"><small>VISIT US AT</small><b>BOOTH <span class="num">#1700</span></b></div>
  <div class="abs brand"><span class="brand-dot"></span><span>Harwick<br>Advisors<br>Team</span></div>
</section>

<section class="ad ad-twitter" aria-label="Twitter ad">
  <div class="photo" role="img" aria-label="Photo of business people talking in a bright office"></div>
  <div class="abs title-box">
    <div class="headline">Industry</div>
    <div class="leaders">Leaders in</div>
    <div class="wlc">White Label Consulting</div>
  </div>
  <div class="abs booth"><small>VISIT US AT</small><b>BOOTH <span class="num">#1700</span></b></div>
</section>

<section class="ad ad-square" aria-label="Instagram ad">
  <div class="abs headline">Industry</div>
  <div class="abs tab">
    <div class="leaders">Leaders in</div>
    <div class="wlc">White Label Consulting</div>
  </div>
  <div class="abs frame"></div>
  <div class="photo" role="img" aria-label="Photo of a team meeting around a conference table"></div>
  <div class="abs booth"><small>VISIT US AT</small><b>BOOTH <span class="num">#1700</span></b></div>
  <div class="abs brand"><span class="brand-dot"></span><span>Harwick<br>Advisors<br>Team</span></div>
</section>

<section class="ad ad-vertical" aria-label="Vertical ad">
  <div class="abs brand"><span class="brand-dot"></span><span>Harwick<br>Advisors<br>Team</span></div>
  <div class="abs headline">Industry</div>
  <div class="abs tab">
    <div class="leaders">Leaders in</div>
    <div class="wlc">White Label Consulting</div>
  </div>
  <div class="abs frame"></div>
  <div class="photo" role="img" aria-label="Photo of a team meeting around a conference table"></div>
  <div class="abs help">
    <h2>We can help you</h2>
    <ul>
      <li><b>Increase</b> Profits</li>
      <li><b>Better</b> - Stronger Relationships</li>
      <li><b>Reduce</b> Costs</li>
      <li><b>Increase</b> Customer Loyalty</li>
      <li><b>Mutual</b> Benefit</li>
      <li><b>Business</b> Appears Larger</li>
    </ul>
  </div>
  <div class="abs booth"><small>VISIT US AT</small><b>BOOTH #1700</b></div>
</section>

</body>
</html>
```